Business Card Design Project

I want a cleaner business card and envelope then what we have now, its too crowded.
Updates

I update with logo, this can be changed anyway you feel it looks best. I also have put gaurantee on there and extended time, this is my first time doing this. Also gave an example of current card

Target Market(s)

a wide array of customers from vantage 400 to small companies and cleints

Industry/Entity Type

Business

Requirements
Must have
• Need to have address, telephone number email
Nice to have
• a sharp professional card that stands out but is still very clean.
Should not have
• Not crazy looking

```html
<!DOCTYPE html>
<html lang="en">
<head>
<meta charset="utf-8">
<title>Harbor Crest Insurance Group – Stationery</title>
<link href="https://fonts.googleapis.com/css2?family=Arimo:ital,wght@0,400;0,700;1,400&display=swap" rel="stylesheet">
<style>
  :root {
    --paper: #ffffff;
    --ink: #111111;
    --rule: #4a4a4a;
    --edge: #222222;
    --mark-light: #d4d4d4;
    --mark-dark: #6e6e6e;
    --gold-dark: #8a7346;
    --gold-light: #cdb47f;
  }
  html, body {
    margin: 0;
    width: 1200px;
    height: 547px;
    overflow: hidden;
    background: var(--paper);
    font-family: "Arimo", Arial, sans-serif;
    color: var(--ink);
  }
  .canvas { position: relative; width: 1200px; height: 547px; }

  .gold-band {
    position: absolute; left: 0; right: 0; bottom: 0;
    background: linear-gradient(180deg, var(--gold-light), var(--gold-dark));
  }

  .brand { display: flex; flex-direction: column; align-items: center; }
  .brand-square {
    background: linear-gradient(135deg, var(--mark-light), var(--mark-dark));
  }
  .brand-name {
    font-weight: 400; color: var(--mark-dark);
    text-align: center; letter-spacing: 1px; line-height: 1.15;
  }
  .return-address { position: absolute; font-style: normal; font-size: 12px; line-height: 15px; }
  .company { font-weight: 700; margin-bottom: 5px; }

  /* Envelope */
  .envelope {
    position: absolute; left: 30px; top: 37px; width: 851px; height: 481px;
    border: 1px solid var(--edge); background: var(--paper); box-sizing: border-box;
  }
  .envelope .gold-band { height: 16px; }
  .envelope .brand { position: absolute; left: 20px; top: 24px; width: 140px; }
  .envelope .brand-square { width: 48px; height: 48px; margin-bottom: 10px; }
  .envelope .brand-name { font-size: 14px; }
  .envelope .divider {
    position: absolute; left: 173px; top: 20px; width: 1px; height: 82px; background: var(--rule);
  }
  .envelope .return-address { left: 191px; top: 28px; }

  /* Business card */
  .card {
    position: absolute; left: 612px; top: 97px; width: 532px; height: 305px;
    border: 1px solid var(--edge); background: var(--paper); box-sizing: border-box;
    transform: rotate(-9deg); overflow: hidden;
  }
  .card .gold-band { height: 18px; }
  .card .brand { position: absolute; left: 14px; top: 34px; width: 170px; }
  .card .brand-square { width: 62px; height: 62px; margin-bottom: 10px; }
  .card .brand-name { font-size: 16px; }
  .person { position: absolute; left: 200px; top: 42px; width: 316px; text-align: center; }
  .person-name { font-size: 26px; font-weight: 700; line-height: 30px; }
  .person-title { font-size: 21px; font-style: italic; line-height: 26px; }
  .contact {
    position: absolute; left: 222px; top: 180px; margin: 0; font-size: 12px; line-height: 15px;
    display: grid; grid-template-columns: 48px auto;
  }
  .contact dt { font-weight: 700; }
  .contact dd { margin: 0; }
  .contact a { color: var(--ink); }
  .card .return-address { left: 22px; top: 166px; }
</style>
</head>
<body>
<div class="canvas">
  <section class="envelope" aria-label="Envelope">
    <div class="brand">
      <div class="brand-square"></div>
      <div class="brand-name">Harbor Crest<br>Insurance Group</div>
    </div>
    <div class="divider"></div>
    <address class="return-address">
      <div class="company">Harbor Crest Insurance Group</div>
      18230 Linden Park Ave.<br>Oak Ridge,<br>MI 48092
    </address>
    <div class="gold-band"></div>
  </section>

  <section class="card" aria-label="Business card">
    <div class="brand">
      <div class="brand-square"></div>
      <div class="brand-name">Harbor Crest<br>Insurance Group</div>
    </div>
    <div class="person">
      <div class="person-name">Marla Quinlan-Hart</div>
      <div class="person-title">Operations Manager</div>
    </div>
    <dl class="contact">
      <dt>Email:</dt><dd><a href="mailto:mquinlan-hart@harborcrestagency.com">mquinlan-hart@harborcrestagency.com</a></dd>
      <dt>Mobile:</dt><dd>555-210-4800 ext 417</dd>
    </dl>
    <address class="return-address">
      <div class="company">Harbor Crest Insurance Group</div>
      18230 Linden Park Ave.<br>Oak Ridge,<br>MI 48092
    </address>
    <div class="gold-band"></div>
  </section>
</div>
</body>
</html>
```